Kestrel Roofing & Restoration Business Card Design

Lookiing for a double sided business card design that will have rounded corners, will look good with Spot UV, Soft Laminate, or Gloss
Front of card should have Logo, Name and Contact Info, License numbers
Back of card should have Logo, maybe other small details

```html
<!DOCTYPE html>
<html lang="en">
<head>
<meta charset="utf-8">
<title>Kestrel Roofing &amp; Restoration – Business Card</title>
<link rel="stylesheet" href="https://fonts.googleapis.com/css2?family=Montserrat:wght@400;500;700;800&display=swap">
<style>
  :root {
    --backdrop: #5a5b5d;
    --card: #1b1b1c;
    --edge: #12a6dc;
    --accent: #14a9e2;
    --ink: #ffffff;
    --ink-soft: #e6e6e6;
    --emboss: #29292a;
  }
  * { box-sizing: border-box; margin: 0; padding: 0; }
  html, body {
    width: 1200px; height: 1200px; overflow: hidden;
    background: var(--backdrop);
    font-family: "Montserrat", sans-serif;
  }
  .sheet { position: relative; width: 1200px; height: 1200px; }

  .card {
    position: absolute; left: 150px;
    width: 900px; height: 514px;
    background: var(--card);
    border-radius: 34px;
    border-bottom: 4px solid var(--edge);
    border-left: 2px solid var(--edge);
    overflow: hidden;
    box-shadow: 0 14px 30px rgba(0,0,0,.45);
  }
  .card--front { top: 62px; }
  .card--back { top: 622px; }

  /* Front */
  .brand-block {
    position: absolute; left: 56px; top: 160px; width: 430px;
    display: flex; align-items: flex-start; gap: 18px;
  }
  .brand-block__square {
    flex: none; width: 28px; height: 28px; margin-top: 10px;
    background: var(--accent);
  }
  .brand-block__name {
    color: var(--ink); font-weight: 800;
    font-size: 42px; line-height: 1.1; letter-spacing: .5px;
    text-transform: uppercase;
  }

  .contact {
    position: absolute; left: 530px; top: 150px;
    color: var(--ink);
  }
  .contact__name {
    color: var(--accent); font-weight: 700; font-size: 38px;
    letter-spacing: 1px; line-height: 1;
  }
  .contact__title {
    font-size: 19px; font-weight: 500; letter-spacing: 1px;
    margin: 10px 0 22px 2px;
  }
  .contact__list { list-style: none; }
  .contact__item {
    display: flex; align-items: center; gap: 12px;
    font-size: 20px; font-weight: 400; color: var(--ink-soft);
    margin-bottom: 12px;
  }
  .contact__icon { width: 22px; height: 22px; flex: none; }
  .contact__item--license { padding-left: 34px; margin-top: 4px; }

  /* Back */
  .pattern {
    position: absolute; inset: 18px 30px;
    display: grid;
    grid-template-columns: repeat(3, 1fr);
    grid-template-rows: repeat(7, 1fr);
    align-items: center; justify-items: center;
  }
  .pattern__item {
    display: flex; align-items: center; gap: 10px;
    color: var(--emboss); font-weight: 800; font-size: 15px;
    line-height: 1.2; letter-spacing: .5px; text-transform: uppercase;
  }
  .pattern__square { width: 12px; height: 12px; background: var(--emboss); flex: none; }
  .pattern__item--lead { color: var(--ink); }
  .pattern__item--lead .pattern__square { background: var(--accent); }
</style>
</head>
<body>
<main class="sheet">

  <section class="card card--front" aria-label="Card front">
    <div class="brand-block">
      <span class="brand-block__square"></span>
      <p class="brand-block__name">Kestrel<br>Roofing &amp;<br>Restoration</p>
    </div>

    <div class="contact">
      <h1 class="contact__name">FULL NAME</h1>
      <p class="contact__title">TITLE</p>
      <ul class="contact__list">
        <li class="contact__item">
          <svg class="contact__icon" viewBox="0 0 24 24" fill="var(--accent)"><path d="M6.6 10.8a15 15 0 0 0 6.6 6.6l2.2-2.2c.3-.3.7-.4 1-.2 1.1.4 2.3.6 3.6.6.6 0 1 .4 1 1V20c0 .6-.4 1-1 1A17 17 0 0 1 3 4c0-.6.4-1 1-1h3.5c.6 0 1 .4 1 1 0 1.3.2 2.5.6 3.6.1.3 0 .7-.2 1z"/></svg>
          (000) 000 0000
        </li>
        <li class="contact__item">
          <svg class="contact__icon" viewBox="0 0 24 24" fill="var(--accent)"><path d="M2 5h20v14H2z M3.5 6.5 12 13l8.5-6.5" stroke="var(--card)" stroke-width="1.6"/></svg>
          email@company.com
        </li>
        <li class="contact__item">
          <svg class="contact__icon" viewBox="0 0 24 24" fill="none" stroke="var(--accent)" stroke-width="1.8"><circle cx="12" cy="12" r="9.5"/><ellipse cx="12" cy="12" rx="4.2" ry="9.5"/><path d="M2.5 12h19M4 7h16M4 17h16"/></svg>
          www.company.com
        </li>
        <li class="contact__item contact__item--license">License: 00000000</li>
      </ul>
    </div>
  </section>

  <section class="card card--back" aria-label="Card back">
    <div class="pattern">
      <p class="pattern__item" aria-hidden="true"><span class="pattern__square"></span>Kestrel Roofing &amp;<br>Restoration</p>
      <p class="pattern__item" aria-hidden="true"><span class="pattern__square"></span>Kestrel Roofing &amp;<br>Restoration</p>
      <p class="pattern__item" aria-hidden="true"><span class="pattern__square"></span>Kestrel Roofing &amp;<br>Restoration</p>
      <p class="pattern__item" aria-hidden="true"><span class="pattern__square"></span>Kestrel Roofing &amp;<br>Restoration</p>
      <p class="pattern__item" aria-hidden="true"><span class="pattern__square"></span>Kestrel Roofing &amp;<br>Restoration</p>
      <p class="pattern__item" aria-hidden="true"><span class="pattern__square"></span>Kestrel Roofing &amp;<br>Restoration</p>
      <p class="pattern__item" aria-hidden="true"><span class="pattern__square"></span>Kestrel Roofing &amp;<br>Restoration</p>
      <p class="pattern__item" aria-hidden="true"><span class="pattern__square"></span>Kestrel Roofing &amp;<br>Restoration</p>
      <p class="pattern__item" aria-hidden="true"><span class="pattern__square"></span>Kestrel Roofing &amp;<br>Restoration</p>
      <p class="pattern__item" aria-hidden="true"><span class="pattern__square"></span>Kestrel Roofing &amp;<br>Restoration</p>
      <p class="pattern__item pattern__item--lead"><span class="pattern__square"></span>Kestrel Roofing &amp;<br>Restoration</p>
      <p class="pattern__item" aria-hidden="true"><span class="pattern__square"></span>Kestrel Roofing &amp;<br>Restoration</p>
      <p class="pattern__item" aria-hidden="true"><span class="pattern__square"></span>Kestrel Roofing &amp;<br>Restoration</p>
      <p class="pattern__item" aria-hidden="true"><span class="pattern__square"></span>Kestrel Roofing &amp;<br>Restoration</p>
      <p class="pattern__item" aria-hidden="true"><span class="pattern__square"></span>Kestrel Roofing &amp;<br>Restoration</p>
      <p class="pattern__item" aria-hidden="true"><span class="pattern__square"></span>Kestrel Roofing &amp;<br>Restoration</p>
      <p class="pattern__item" aria-hidden="true"><span class="pattern__square"></span>Kestrel Roofing &amp;<br>Restoration</p>
      <p class="pattern__item" aria-hidden="true"><span class="pattern__square"></span>Kestrel Roofing &amp;<br>Restoration</p>
      <p class="pattern__item" aria-hidden="true"><span class="pattern__square"></span>Kestrel Roofing &amp;<br>Restoration</p>
      <p class="pattern__item" aria-hidden="true"><span class="pattern__square"></span>Kestrel Roofing &amp;<br>Restoration</p>
      <p class="pattern__item" aria-hidden="true"><span class="pattern__square"></span>Kestrel Roofing &amp;<br>Restoration</p>
    </div>
  </section>

</main>
</body>
</html>
```